KVT Website (Halcyon Guard Networks)

We need a web design for an established company in Dubai, U.A.E, called Halcyon Guard Network. We provide a completed solutions in ICT-Information and Communication Technology (Computer, Networking, IP Telephony, Software and Hardware) and Security Systems (CCTV, Access Control, and System Integrator), our Services include Consultancy Planning and Design, Value Added Distribution, Implementation and Execution, Operations and Maintenance, Training and Development. We help our Clients to Develop and Secure their infrastructure. We would like to see design that use our logo theme, reflect our solutions and services, communicate to enterprise Technology and Security. Website must be responsive, Dynamic, symmetry or asymmetry or both.
Regards,

Target Market(s)

UAE

Industry/Entity Type

It Company

Coding

Coded - Design and coding required

Number of Pages Required

5+ page

Font styles to use
Sans Serif

Requirements
Must have
• Logo Theme, social media logos and links,
Nice to have
• Big blogs and banners
Should not have
• Many colors or congested design

```html
<!DOCTYPE html>
<html lang="en">
<head>
<meta charset="utf-8">
<title>Halcyon Guard Networks</title>
<link href="https://fonts.googleapis.com/css2?family=Open+Sans:wght@400;600;700&display=swap" rel="stylesheet">
<style>
:root{
  --yellow:#f3be1c;
  --dark:#2d2f32;
  --darker:#222426;
  --band:#55585c;
  --grey:#8b8e92;
  --light:#eeeeee;
  --text:#555;
  --white:#fff;
}
*{box-sizing:border-box;margin:0;padding:0}
html,body{width:1200px;height:2760px;overflow:hidden}
body{font-family:"Open Sans",Arial,sans-serif;color:var(--text);background:var(--white);position:relative}
section,header,footer{position:absolute;left:0;width:1200px}
.header{top:0;height:152px;background:var(--dark)}
.brand{position:absolute;left:30px;top:8px;width:300px;height:132px;background:#45484c;display:flex;align-items:center;gap:14px;padding:0 22px}
.brand-dot{width:52px;height:52px;border-radius:50%;border:4px solid var(--yellow);flex:none}
.brand-name{color:var(--yellow);font-weight:700;font-size:26px;line-height:1.1}
.topbar{position:absolute;right:40px;top:14px;display:flex;align-items:center;gap:10px;color:#ddd;font-size:15px}
.social{width:26px;height:26px;background:#6a6d71;border-radius:3px}
.phone{display:flex;align-items:center;gap:8px;margin-left:24px;color:var(--yellow);font-weight:600}
.nav{position:absolute;right:40px;top:96px;display:flex;gap:8px}
.nav a{color:#fff;text-decoration:none;font-size:18px;font-weight:600;padding:10px 20px;border-radius:3px}
.nav a.active{background:var(--yellow);color:var(--dark)}
.hero{top:152px;height:408px;background:linear-gradient(100deg,#cfd0cc 0%,#e9e9e6 40%,#b9bbb7 70%,#8f918d 100%)}
.hero-caption{position:absolute;left:240px;top:300px;width:680px;padding:16px 22px;background:rgba(40,40,40,.72);color:var(--yellow);font-weight:700;font-size:24px;line-height:1.35}
.hero-arrows{position:absolute;left:640px;top:280px;display:flex;gap:6px}
.hero-arrows span{width:28px;height:28px;background:rgba(30,30,30,.8);color:#fff;display:flex;align-items:center;justify-content:center;font-size:16px}
.features{top:560px;height:260px;display:flex;justify-content:center;padding:30px 120px 0}
.feature{width:240px;text-align:center;padding:0 18px}
.feature + .feature{border-left:1px solid #e2e2e2}
.feature h3{font-size:18px;color:#333;margin:14px 0 8px;font-weight:700}
.feature p{font-size:13px;line-height:1.5;color:#888}
.info{top:820px;height:320px;background:#f3f3f3;padding:30px 120px;display:flex;gap:40px}
.about{flex:1.4}
.videos{flex:1}
.sec-title{font-size:28px;font-weight:700;color:#444;margin-bottom:14px}
.sec-title em{font-style:normal;color:var(--yellow)}
.about p{font-size:13px;line-height:1.6;color:#777;margin-bottom:10px}
.more{font-size:14px;color:#444;font-weight:600}
.video{height:200px;background:linear-gradient(135deg,#c9c9c9,#8e8e8e);position:relative}
.video-bar{position:absolute;left:0;right:0;bottom:0;height:26px;background:#222}
.play{position:absolute;left:50%;top:45%;transform:translate(-50%,-50%);width:60px;height:60px;border-radius:50%;background:rgba(20,20,20,.8)}
.play:after{content:"";position:absolute;left:24px;top:18px;border-left:18px solid #fff;border-top:12px solid transparent;border-bottom:12px solid transparent}
.services{top:1140px;height:320px;background:var(--band);text-align:center;padding-top:34px}
.services .sec-title{color:#fff}
.svc-row{display:flex;justify-content:center;gap:30px;margin-top:20px}
.svc{width:170px;color:#fff;font-size:16px;line-height:1.3}
.svc-icon{width:118px;height:118px;border-radius:50%;background:#8f9296;margin:0 auto 12px;display:flex;align-items:center;justify-content:center}
.svc.active .svc-icon{background:var(--yellow);box-shadow:0 0 0 6px rgba(243,190,28,.35)}
.svc.active{color:var(--yellow)}
.partners{top:1460px;height:220px;text-align:center;padding-top:36px}
.logo-row{display:flex;align-items:center;justify-content:center;gap:36px;margin-top:30px}
.arrow{font-size:28px;color:#333;font-weight:700}
.brandname{font-size:20px;font-weight:700;color:#444;width:120px;text-align:center}
.projects{top:1680px;height:560px;text-align:center;padding-top:34px}
.grid{display:grid;grid-template-columns:repeat(3,260px);gap:58px 60px;justify-content:center;margin-top:24px}
.tile{height:170px;position:relative}
.tile-label{position:absolute;inset:0;display:flex;align-items:center;justify-content:center;color:#fff;font-size:24px;font-weight:600;background:rgba(60,60,60,.45)}
.clients{top:2240px;height:220px;background:var(--light);text-align:center;padding-top:30px}
.client-row{display:flex;align-items:center;justify-content:center;gap:30px;margin-top:32px}
.diamond{width:26px;height:26px;background:var(--yellow);transform:rotate(45deg)}
.client{font-size:18px;font-weight:700;color:#3a6a8a;width:150px;white-space:nowrap}
.footer{top:2460px;height:260px;background:var(--darker);padding:36px 120px;display:flex;gap:60px;color:#bbb;font-size:13px}
.footer h4{color:#fff;font-size:15px;margin-bottom:12px}
.footer ul{list-style:none;line-height:1.9}
.contact p{margin-bottom:8px;display:flex;gap:8px;align-items:center}
.signup input{display:block;width:220px;height:26px;margin-bottom:8px;border:0;background:#fff}
.signup .btn{background:var(--yellow);color:var(--dark);font-weight:700;padding:5px 14px;display:inline-block}
.foot-brand{margin-left:auto;width:220px;height:170px;background:#45484c;display:flex;flex-direction:column;align-items:center;justify-content:center;gap:10px}
.foot-brand .brand-name{font-size:20px;text-align:center}
.copy{position:absolute;top:2720px;left:0;width:1200px;height:40px;background:#161718;color:#888;font-size:12px;padding:12px 120px}
</style>
</head>
<body>
<header class="header">
  <div class="brand"><span class="brand-dot"></span><span class="brand-name">Halcyon Guard<br>Networks</span></div>
  <div class="topbar">Follow us on
    <span class="social" aria-label="Social link"></span><span class="social" aria-label="Social link"></span><span class="social" aria-label="Social link"></span><span class="social" aria-label="Social link"></span>
    <span class="phone"><svg width="18" height="18" viewBox="0 0 24 24"><circle cx="12" cy="12" r="11" fill="#f3be1c"/><path d="M8 6l2 3-1 2c1 2 2 3 4 4l2-1 3 2-1 2c-5 0-10-5-10-10z" fill="#2d2f32"/></svg>800 555 0142</span>
  </div>
  <nav class="nav"><a class="active">Home</a><a>About Us</a><a>Services</a><a>Testimonials</a><a>Contact Us</a></nav>
</header>

<section class="hero" role="img" aria-label="Office desk with an IP desk phone and a plant, person working in the background">
  <div class="hero-arrows"><span>‹</span><span>›</span></div>
  <div class="hero-caption">We Provide A Complete Solution In ICT Information, Communication Technology And Security Systems</div>
</section>

<section class="features">
  <div class="feature">
    <svg width="70" height="70" viewBox="0 0 70 70"><rect x="15" y="15" width="40" height="40" transform="rotate(45 35 35)" fill="none" stroke="#f3be1c" stroke-width="4"/><rect x="26" y="27" width="18" height="16" rx="2" fill="#444"/></svg>
    <h3>IP Telephony System</h3><p>Clear voice lines and unified calling for every office and branch team.</p>
  </div>
  <div class="feature">
    <svg width="70" height="70" viewBox="0 0 70 70"><rect x="15" y="15" width="40" height="40" transform="rotate(45 35 35)" fill="none" stroke="#f3be1c" stroke-width="4"/><path d="M35 24l10 4v7c0 6-4 10-10 12-6-2-10-6-10-12v-7z" fill="#444"/></svg>
    <h3>Security Systems</h3><p>CCTV, access control and full integration for safe and secure sites.</p>
  </div>
  <div class="feature">
    <svg width="70" height="70" viewBox="0 0 70 70"><rect x="15" y="15" width="40" height="40" transform="rotate(45 35 35)" fill="none" stroke="#f3be1c" stroke-width="4"/><circle cx="35" cy="32" r="7" fill="#444"/><path d="M28 35l7 12 7-12z" fill="#444"/></svg>
    <h3>Tracking and GPS</h3><p>Live fleet and asset tracking with accurate location reports each day.</p>
  </div>
  <div class="feature">
    <svg width="70" height="70" viewBox="0 0 70 70"><rect x="15" y="15" width="40" height="40" transform="rotate(45 35 35)" fill="none" stroke="#f3be1c" stroke-width="4"/><rect x="25" y="26" width="20" height="14" fill="#444"/><rect x="30" y="41" width="10" height="4" fill="#444"/></svg>
    <h3>Online Services</h3><p>Hosted software, support portals and cloud tools for growing firms.</p>
  </div>
</section>

<section class="info">
  <div class="about">
    <h2 class="sec-title">About <em>Halcyon Guard Networks</em></h2>
    <p>We are an established technology partner in Dubai delivering computer, networking, IP telephony, software and hardware solutions. Our engineers plan, build and support systems that keep enterprises connected and running every day across the region.</p>
    <p>Our security division designs CCTV, access control and integrated platforms that protect people and assets. From first survey to long term care, we help clients develop and secure their infrastructure with trusted brands and skilled teams.</p>
    <span class="more">Read More ›</span>
  </div>
  <div class="videos">
    <h2 class="sec-title">Latest <em>Videos</em></h2>
    <div class="video" role="img" aria-label="Video still of a server room"><span class="play"></span><span class="video-bar"></span></div>
  </div>
</section>

<section class="services">
  <h2 class="sec-title">Our <em>Services</em></h2>
  <div class="svc-row">
    <div class="svc active"><div class="svc-icon"><svg width="56" height="56" viewBox="0 0 56 56"><circle cx="28" cy="28" r="20" fill="none" stroke="#fff" stroke-width="4"/><circle cx="28" cy="28" r="8" fill="#fff"/></svg></div>Consultancy<br>Planning and Design</div>
    <div class="svc"><div class="svc-icon"><svg width="56" height="56" viewBox="0 0 56 56"><rect x="12" y="16" width="32" height="26" fill="#fff"/><rect x="12" y="12" width="32" height="6" fill="#ddd"/></svg></div>Value<br>Added Distribution</div>
    <div class="svc"><div class="svc-icon"><svg width="56" height="56" viewBox="0 0 56 56"><circle cx="22" cy="30" r="11" fill="none" stroke="#fff" stroke-width="6" stroke-dasharray="5 3"/><circle cx="38" cy="18" r="7" fill="none" stroke="#fff" stroke-width="5" stroke-dasharray="4 3"/></svg></div>Implementation<br>and Execution</div>
    <div class="svc"><div class="svc-icon"><svg width="56" height="56" viewBox="0 0 56 56"><path d="M14 14l28 28M42 14L14 42" stroke="#fff" stroke-width="6" stroke-linecap="round"/></svg></div>Operations<br>and Maintenance</div>
    <div class="svc"><div class="svc-icon"><svg width="56" height="56" viewBox="0 0 56 56"><circle cx="20" cy="20" r="7" fill="#fff"/><circle cx="36" cy="20" r="7" fill="#fff"/><path d="M8 42c0-8 6-12 12-12s12 4 12 12zM26 42c0-8 6-12 10-12s12 4 12 12z" fill="#fff"/></svg></div>Training<br>and Development</div>
  </div>
</section>

<section class="partners">
  <h2 class="sec-title">Key <em>Partners</em></h2>
  <div class="logo-row">
    <span class="arrow">‹</span>
    <span class="brandname">Corvane</span><span class="brandname">Veltrix</span><span class="brandname">Nodeline</span><span class="brandname">Brightsoft</span><span class="brandname">Teralink</span><span class="brandname">Sentrel</span>
    <span class="arrow">›</span>
  </div>
</section>

<section class="projects">
  <h2 class="sec-title">Major <em>Projects</em></h2>
  <div class="grid">
    <div class="tile" role="img" aria-label="Server room project" style="background:linear-gradient(135deg,#9a9a9a,#6d6d6d)"><div class="tile-label">Lorem ipsum dolor</div></div>
    <div class="tile" role="img" aria-label="Network cabinet installation" style="background:linear-gradient(135deg,#d8d6cf,#9d9a90)"></div>
    <div class="tile" role="img" aria-label="Container data centre" style="background:linear-gradient(135deg,#c9a35c,#8d6e3a)"></div>
    <div class="tile" role="img" aria-label="Rack corridor" style="background:linear-gradient(135deg,#e2e2e2,#a5a5a8)"></div>
    <div class="tile" role="img" aria-label="Equipment room" style="background:linear-gradient(135deg,#d9d3c4,#8f8a7c)"></div>
    <div class="tile" role="img" aria-label="Control room interior" style="background:linear-gradient(135deg,#e6e6d8,#b8c4a0)"></div>
  </div>
</section>

<section class="clients">
  <h2 class="sec-title">Major <em>Clients</em></h2>
  <div class="client-row">
    <span class="diamond"></span>
    <span class="client">Westgate Marine</span><span class="client">Qarsa</span><span class="client">Lumora</span><span class="client">Pelion</span><span class="client">Marbell</span>
    <span class="diamond"></span>
  </div>
</section>

<footer class="footer">
  <div><h4>Quick Link</h4><ul><li>Home</li><li>About Us</li><li>Services</li><li>Testimonials</li><li>Contact Us</li></ul></div>
  <div class="contact"><h4>Contact Address</h4>
    <p><svg width="12" height="16" viewBox="0 0 12 16"><path d="M6 0a6 6 0 0 1 6 6c0 4-6 10-6 10S0 10 0 6a6 6 0 0 1 6-6z" fill="#f3be1c"/></svg>Halcyon Guard Networks<br>Office 204, Bay Tower, Dubai</p>
    <p><svg width="12" height="12" viewBox="0 0 12 12"><circle cx="6" cy="6" r="6" fill="#f3be1c"/></svg>800 555 0142</p>
    <p><svg width="12" height="12" viewBox="0 0 12 12"><circle cx="6" cy="6" r="6" fill="#f3be1c"/></svg>800 555 0143</p>
    <p><svg width="12" height="12" viewBox="0 0 12 12"><rect width="12" height="9" y="1" fill="#f3be1c"/></svg>info@halcyonguard.example</p>
  </div>
  <div class="signup"><h4>Newsletter Signup</h4><p style="margin-bottom:10px">Get our latest news and updates.</p><input aria-label="Name"><input aria-label="Email"><span class="btn">Subscribe</span></div>
  <div class="foot-brand"><span class="brand-dot"></span><span class="brand-name">Halcyon Guard<br>Networks</span></div>
</footer>
<div class="copy">Copyright 2024 by Halcyon Guard Networks. All Rights Reserved.</div>
</body>
</html>
```